Mandala-like Graphic for Ecosystem of Well-Being

I have created a simple graphic for a framework I use with clients and potential clients. I would like it to look more polished, professional, and customized. (As opposed to non-graphic designer created it on Canva or Powrepoint) I would like to possibly integrate my brand colors---or one of my brand colors. https://tintcrate.net/color-palette-5817/ The dark blue is the one to definitely use. I do not want it looking to feminine. I do want different colors for the 5 elements: Purpose, Mental, Physical, Emotional, Social.

Target Market(s)

Working professionals.

Font styles to use
Serif
Other font styles liked:
• Playfair Display

Requirements
Must have
• 4 Overlapping circles with one circle in center that says Purpose
Other 4 circles labeled Physical, Emotional, Mental, Social
Mandala-like design

**I added an attachment with colors I use when marketing this course.**
Nice to have
• Playfair Display font

```html
<!DOCTYPE html>
<html lang="en">
<head>
<meta charset="UTF-8">
<title>Ecosystem of Well-Being</title>
<link rel="stylesheet" href="https://fonts.googleapis.com/css2?family=Tinos:wght@700&display=swap">
<style>
  :root {
    --paper: #ffffff;
    --ink: #111111;
    --navy: #2f5a9e;
    --physical-ring: #e2b800;
    --mental-ring: #d41a5c;
    --emotional-ring: #4f9a2a;
    --social-ring: #7a3580;
    --purpose-ring: #2f5a9e;
    --link-top: #3867ad;
    --link-right: #d0387f;
    --link-bottom: #8a4592;
    --link-left: #ef7a1d;
  }
  html, body {
    margin: 0;
    padding: 0;
    width: 1200px;
    height: 1200px;
    overflow: hidden;
    background: var(--paper);
  }
  .wellbeing-diagram {
    display: block;
    width: 1200px;
    height: 1200px;
  }
  .link-ring { fill: none; stroke-width: 20; }
  .link-ring--top { stroke: var(--link-top); }
  .link-ring--right { stroke: var(--link-right); }
  .link-ring--bottom { stroke: var(--link-bottom); }
  .link-ring--left { stroke: var(--link-left); }
  .element-face { stroke-width: 24; }
  .element--physical .element-face { stroke: var(--physical-ring); }
  .element--mental .element-face { stroke: var(--mental-ring); }
  .element--emotional .element-face { stroke: var(--emotional-ring); }
  .element--social .element-face { stroke: var(--social-ring); }
  .element--purpose .element-face { stroke: var(--purpose-ring); }
  .element-label {
    font-family: "Tinos", "Times New Roman", serif;
    font-weight: 700;
    font-size: 52px;
    fill: var(--ink);
    text-anchor: middle;
  }
</style>
</head>
<body>
<svg class="wellbeing-diagram" viewBox="0 0 1200 1200" xmlns="http://www.w3.org/2000/svg" role="img" aria-label="Ecosystem of well-being: Purpose at the centre, surrounded by Physical, Mental, Emotional and Social">
  <defs>
    <radialGradient id="fill-physical" cx="50%" cy="45%" r="55%">
      <stop offset="0" stop-color="#ffffff"/>
      <stop offset="0.55" stop-color="#ffe86a"/>
      <stop offset="1" stop-color="#f9c800"/>
    </radialGradient>
    <radialGradient id="fill-mental" cx="50%" cy="45%" r="55%">
      <stop offset="0" stop-color="#ffffff"/>
      <stop offset="0.55" stop-color="#f27fa8"/>
      <stop offset="1" stop-color="#e3175f"/>
    </radialGradient>
    <radialGradient id="fill-emotional" cx="50%" cy="45%" r="55%">
      <stop offset="0" stop-color="#ffffff"/>
      <stop offset="0.55" stop-color="#a8d57e"/>
      <stop offset="1" stop-color="#5aac24"/>
    </radialGradient>
    <radialGradient id="fill-social" cx="50%" cy="45%" r="55%">
      <stop offset="0" stop-color="#ffffff"/>
      <stop offset="0.55" stop-color="#bf8fc0"/>
      <stop offset="1" stop-color="#85357f"/>
    </radialGradient>
    <radialGradient id="fill-purpose" cx="50%" cy="45%" r="55%">
      <stop offset="0" stop-color="#ffffff"/>
      <stop offset="0.55" stop-color="#97b0d6"/>
      <stop offset="1" stop-color="#3563a8"/>
    </radialGradient>
  </defs>

  <g class="links">
    <circle class="link-ring link-ring--top" cx="600" cy="258" r="167"/>
    <circle class="link-ring link-ring--right" cx="942" cy="600" r="167"/>
    <circle class="link-ring link-ring--bottom" cx="600" cy="942" r="167"/>
    <circle class="link-ring link-ring--left" cx="258" cy="600" r="167"/>
  </g>

  <g class="element element--physical">
    <circle class="element-face" cx="385" cy="385" r="205" fill="url(#fill-physical)"/>
    <text class="element-label" x="385" y="375">PHYSICAL</text>
  </g>

  <g class="element element--mental">
    <circle class="element-face" cx="815" cy="385" r="205" fill="url(#fill-mental)"/>
    <text class="element-label" x="812" y="375">MENTAL</text>
  </g>

  <g class="element element--emotional">
    <circle class="element-face" cx="385" cy="815" r="205" fill="url(#fill-emotional)"/>
    <text class="element-label" x="385" y="862">EMOTIONAL</text>
  </g>

  <g class="element element--social">
    <circle class="element-face" cx="815" cy="815" r="205" fill="url(#fill-social)"/>
    <text class="element-label" x="812" y="862">SOCIAL</text>
  </g>

  <g class="element element--purpose">
    <circle class="element-face" cx="600" cy="600" r="205" fill="url(#fill-purpose)"/>
    <text class="element-label" x="597" y="618">PURPOSE</text>
  </g>
</svg>
</body>
</html>
```